Luxury Bath Flyer

I would like to have a professional Flyer, which would describe a beautiful atmospheric luxury-Bath situation. I am sending you a( screenshot) Flyer Proposal, which shoes my intention and wish how I would like to have it. Please note that Ästhetik and a professional Flyer is very important to me. If possible send a psd.file or a indesign file, in case of we gonna need to change the text. You are also free to make 2 different proposals and one as you would suggest.?(I send you couple pictures, but the main one which I choose on the pdf file, please keep that, it is called " KR-71" - If there is a question please let me know. Looking forward to receive an amazing artwork.Kind Regards Merle
Look and feel
Each slider illustrates characteristics of the customer's brand and the style your logo design should communicate.

```html
<!DOCTYPE html>
<html lang="de">
<head>
<meta charset="utf-8">
<title>Luxury Bath Flyer</title>
<link href="https://fonts.googleapis.com/css2?family=Lato:wght@400;700;900&display=swap" rel="stylesheet">
<style>
  :root{
    --stage:#e4e4e4;
    --dark:#2f2e30;
    --gold:#b39b5f;
    --gold-light:#c4ad72;
    --gold-deep:#a28a50;
    --white:#ffffff;
    --ink:#2b2b2b;
    --label:rgba(58,56,58,.88);
  }
  *{margin:0;padding:0;box-sizing:border-box}
  html,body{width:1200px;height:800px;overflow:hidden;background:var(--stage);font-family:"Lato",sans-serif}
  .canvas{position:relative;width:1200px;height:800px}
  .flyer{
    position:absolute;left:341px;top:30px;width:450px;height:644px;
    transform:scale(1.149);transform-origin:top left;
    background:var(--white);overflow:hidden;
    box-shadow:0 6px 18px rgba(0,0,0,.18);
  }
  .abs{position:absolute}
  .hero-photo{left:0;top:0;width:450px;height:289px;
    background:linear-gradient(180deg,#cfcac2 0%,#bdb3a6 35%,#8a6a4d 70%,#5a4534 100%)}
  .label{left:18px;color:var(--white);padding:0 8px;display:flex;align-items:center;white-space:nowrap}
  .label--title{top:45px;height:30px;background:var(--label);font-size:17.5px}
  .label--gold{top:82px;height:32px;background:rgba(179,155,95,.9);font-size:17px}
  .label--small{top:121px;height:28px;background:var(--label);font-size:12.5px}
  .brand{right:18px;top:22px;display:flex;align-items:center;gap:6px;color:var(--dark);font-weight:900;font-size:17px;line-height:1}
  .brand-dot{width:14px;height:14px;border-radius:50%;background:var(--dark)}
  .band-gold{left:0;top:287px;width:266px;height:4px;background:var(--gold)}
  .dark-panel{left:0;top:291px;width:266px;height:158px;background:var(--dark)}
  .inset-photo{left:19px;top:257px;width:229px;height:145px;border:3px solid var(--gold);
    background:linear-gradient(160deg,#ece9e4 0%,#d8cfc2 45%,#a9886a 100%)}
  .services-title{left:23px;top:416px;color:var(--gold);font-weight:700;font-size:19px}
  .services-list{left:22px;top:457px;list-style:none;font-size:12.6px;line-height:14.3px;color:var(--ink)}
  .side-panel{left:266px;top:217px;width:184px;height:427px;background:var(--dark)}
  .side-photo{left:266px;top:217px;width:184px;height:253px;border:3px solid var(--gold);border-right:none;
    background:linear-gradient(180deg,#e6e4e0 0%,#cfccc6 55%,#5b5a5c 85%,#3a393b 100%)}
  .benefits-title{left:300px;top:485px;color:var(--gold);font-weight:700;font-size:18px}
  .benefits{left:278px;top:518px;list-style:none;color:var(--white);font-size:10.8px}
  .benefits li{display:flex;align-items:center;gap:7px;height:24px}
  .address{left:278px;top:594px;display:flex;gap:9px;color:var(--white);font-size:10.8px;line-height:13px}
  .callbox{left:20px;top:535px;width:222px;height:50px;display:flex}
  .callbox-icon{width:50px;background:var(--gold-deep);display:flex;align-items:center;justify-content:center}
  .callbox-text{flex:1;background:var(--gold-light);color:var(--white);padding:5px 0 0 9px}
  .callbox-tag{font-size:9.5px;font-weight:700;display:block}
  .callbox-phone{font-size:23px;font-weight:900;letter-spacing:.3px;display:block;line-height:25px}
  .contact{top:605px;display:flex;align-items:center;gap:6px;font-size:10.5px;color:var(--ink)}
  .contact--mail{left:21px}
  .contact--web{left:143px}
</style>
</head>
<body>
<div class="canvas">
  <article class="flyer">
    <div class="abs hero-photo" role="img" aria-label="Luxuriöses Badezimmer mit freistehender Wanne, Holzboden und Wandschrank"></div>

    <div class="abs label label--title">Ihr exklusives Bad zum Fixpreis!</div>
    <div class="abs label label--gold">Wir montieren für Sie...</div>
    <div class="abs label label--small">und das „Alles aus einer Hand“!</div>

    <div class="abs brand"><span>Lindenbad</span><span class="brand-dot"></span></div>

    <div class="abs band-gold"></div>
    <div class="abs dark-panel"></div>
    <div class="abs inset-photo" role="img" aria-label="Waschtisch mit Aufsatzbecken vor Mosaikfliesen"></div>

    <h2 class="abs services-title">Unsere Services</h2>
    <ul class="abs services-list">
      <li>Markenbäder zum Online Preis</li>
      <li>Wir montieren für Sie</li>
      <li>Funktionalität und Ästhetik</li>
      <li>Komplettlösungen mit rasche Umsetzung</li>
    </ul>

    <div class="abs side-panel"></div>
    <div class="abs side-photo" role="img" aria-label="Modernes Bad mit Handtuchheizkörper und hellen Wandfliesen"></div>

    <h2 class="abs benefits-title">Ihre Vorteile</h2>
    <ul class="abs benefits">
      <li><svg width="15" height="15" viewBox="0 0 16 16"><circle cx="8" cy="8" r="6.5" fill="none" stroke="#b39b5f" stroke-width="1.6"/><path d="M4.5 8.2l2.4 2.4L13.5 3.6" fill="none" stroke="#b39b5f" stroke-width="2"/></svg>Individuelle Badplanung</li>
      <li><svg width="15" height="15" viewBox="0 0 16 16"><circle cx="8" cy="8" r="6.5" fill="none" stroke="#b39b5f" stroke-width="1.6"/><path d="M4.5 8.2l2.4 2.4L13.5 3.6" fill="none" stroke="#b39b5f" stroke-width="2"/></svg>Eigene Handwerker vor Ort</li>
      <li><svg width="15" height="15" viewBox="0 0 16 16"><circle cx="8" cy="8" r="6.5" fill="none" stroke="#b39b5f" stroke-width="1.6"/><path d="M4.5 8.2l2.4 2.4L13.5 3.6" fill="none" stroke="#b39b5f" stroke-width="2"/></svg>Traumbad erlebniss</li>
    </ul>

    <div class="abs address">
      <svg width="14" height="14" viewBox="0 0 16 16"><circle cx="8" cy="8" r="8" fill="#fff"/><path d="M8 3.5a3 3 0 0 0-3 3c0 2.2 3 5.8 3 5.8s3-3.6 3-5.8a3 3 0 0 0-3-3z" fill="#2f2e30"/><circle cx="8" cy="6.5" r="1.1" fill="#fff"/></svg>
      <span>Ulmenweg 14,<br>2360 Talheim am Bach</span>
    </div>

    <div class="abs callbox">
      <div class="callbox-icon">
        <svg width="32" height="28" viewBox="0 0 32 28"><path d="M3 3h18v12H11l-5 4v-4H3z" fill="none" stroke="#fff" stroke-width="2" stroke-linejoin="round"/><path d="M23 9h6v11h-3v3l-4-3h-8v-3" fill="none" stroke="#fff" stroke-width="2" stroke-linejoin="round"/><circle cx="8" cy="9" r="1.3" fill="#fff"/><circle cx="12" cy="9" r="1.3" fill="#fff"/><circle cx="16" cy="9" r="1.3" fill="#fff"/></svg>
      </div>
      <div class="callbox-text">
        <span class="callbox-tag">Einfach &amp; schnell zum Traumbad</span>
        <span class="callbox-phone">0800 314 628</span>
      </div>
    </div>

    <div class="abs contact contact--mail">
      <svg width="16" height="16" viewBox="0 0 16 16"><circle cx="8" cy="8" r="8" fill="#b39b5f"/><rect x="4" y="5" width="8" height="6" fill="none" stroke="#fff" stroke-width="1.2"/><path d="M4 5l4 3.2L12 5" fill="none" stroke="#fff" stroke-width="1.2"/></svg>
      <span>office@lindenbad.at</span>
    </div>
    <div class="abs contact contact--web">
      <svg width="16" height="16" viewBox="0 0 16 16"><circle cx="8" cy="8" r="8" fill="#b39b5f"/><circle cx="8" cy="8" r="4.5" fill="none" stroke="#fff" stroke-width="1.1"/><ellipse cx="8" cy="8" rx="2" ry="4.5" fill="none" stroke="#fff" stroke-width="1.1"/><path d="M3.5 8h9" stroke="#fff" stroke-width="1.1"/></svg>
      <span>www.lindenbad.at</span>
    </div>
  </article>
</div>
</body>
</html>
```